Med Spa business card design with logo

Need a logo design and business card for our new company Velora Skinworks Med Spa. We are a medical office that deals with high end clients. We offer them skin care products which include NERVAX, lip augmentation, and various laser for the skin. I king of like the logo attached, maybe something along those lines but also open to any logo concept.
Updates

Target Market(s)

Out target audience are male and females in the age range of 21-80 years of age

Industry/Entity Type

Medical

Contact Information for Business Card

woukd like front of card to have logo and business name VELORA SKINWORKS MEDSPA. Back of card employee name and phone number along with instagram logo and user name

Font styles to use
Serif
Sans Serif

Requirements
Must have
• prefer monochromatic look white, black, gold
Should not have
• not too colorful

```html
<!DOCTYPE html>
<html lang="en">
<head>
<meta charset="utf-8">
<title>Velora Skinworks Med Spa – Business Card</title>
<link href="https://fonts.googleapis.com/css2?family=Poppins:wght@300&family=Lato:wght@400;700&display=swap" rel="stylesheet">
<style>
  :root{
    --backdrop:#2b2724;
    --card-black:#1c1c1d;
    --card-white:#ffffff;
    --gold:#c0913a;
    --gold-soft:#d4ae5f;
    --ink:#222222;
    --ink-soft:#3a3a3a;
    --rule-light:#e9e9e9;
    --rule-dark:#9a9a9a;
  }
  *{margin:0;padding:0;box-sizing:border-box}
  html,body{width:1200px;height:780px;overflow:hidden;background:var(--backdrop)}
  .stage{width:1200px;height:780px;position:relative;display:flex;align-items:center;justify-content:center;gap:60px}
  .card{width:520px;height:300px;position:relative;border-radius:2px}
  .card--front{background:var(--card-black);color:var(--rule-light)}
  .card--back{background:var(--card-white);color:var(--ink);display:flex}

  .brand{display:flex;flex-direction:column;align-items:center;font-family:"Poppins",sans-serif;font-weight:300}
  .brand__mark{width:46px;height:46px;border-radius:50%;background:var(--gold);margin-bottom:16px}
  .brand__name{font-size:27px;letter-spacing:.5px;line-height:1}
  .brand__sub{display:flex;align-items:center;gap:10px;font-size:19px;margin-top:4px;line-height:1}
  .brand__rule{display:block;width:54px;height:1px;background:currentColor}

  .card--front .brand{position:absolute;left:0;right:0;top:70px}
  .card--front .brand__name,.card--front .brand__sub{color:var(--rule-light)}
  .website{position:absolute;left:0;right:0;top:210px;text-align:center;font-family:"Lato",sans-serif;font-size:13px;color:var(--rule-light);letter-spacing:.3px}
  .website span{color:var(--gold-soft)}

  .card--back .brand{width:290px;justify-content:center;color:var(--ink)}
  .card--back .brand__name{font-size:25px}
  .card--back .brand__sub{font-size:18px}
  .divider{width:1px;background:var(--rule-dark);margin:40px 0}
  .contact{flex:1;padding:62px 0 0 26px;font-family:"Lato",sans-serif;color:var(--ink)}
  .contact__name{font-size:17px;color:var(--gold);letter-spacing:.5px;font-weight:400}
  .contact__role{font-size:13px;color:var(--ink-soft);margin-bottom:12px}
  .contact__line{display:flex;align-items:center;gap:7px;font-size:13px;margin-bottom:3px}
  .icon{width:15px;height:15px;background:var(--gold);border-radius:2px;display:flex;align-items:center;justify-content:center}
  .icon svg{width:10px;height:10px}
  .contact__address{font-size:13px;line-height:1.45;margin-top:8px}
</style>
</head>
<body>
<main class="stage">
  <section class="card card--front" aria-label="Card front">
    <div class="brand">
      <span class="brand__mark"></span>
      <span class="brand__name">Velora Skinworks</span>
      <span class="brand__sub"><i class="brand__rule"></i>Med Spa<i class="brand__rule"></i></span>
    </div>
    <p class="website">www.<span>veloraskin</span>.com</p>
  </section>

  <section class="card card--back" aria-label="Card back">
    <div class="brand">
      <span class="brand__mark"></span>
      <span class="brand__name">Velora Skinworks</span>
      <span class="brand__sub"><i class="brand__rule"></i>Med Spa<i class="brand__rule"></i></span>
    </div>
    <div class="divider"></div>
    <div class="contact">
      <p class="contact__name">MARA ELLISON</p>
      <p class="contact__role">Director</p>
      <p class="contact__line"><span class="icon"><svg viewBox="0 0 10 10"><path d="M2 1h2l1 2.2-1.2.8a5 5 0 0 0 2.2 2.2l.8-1.2L9 6v2a1 1 0 0 1-1 1A7 7 0 0 1 1 2a1 1 0 0 1 1-1z" fill="#fff"/></svg></span>(02) 4817 3390</p>
      <p class="contact__line"><span class="icon"><svg viewBox="0 0 10 10"><rect x="1" y="2" width="8" height="6" rx="1" fill="#fff"/><rect x="3" y="3.5" width="4" height="3" fill="#c0913a"/></svg></span>(02) 4817 3391</p>
      <p class="contact__line"><span class="icon"><svg viewBox="0 0 10 10"><rect x="1" y="2" width="8" height="6" fill="#fff"/><path d="M1 2l4 3.3L9 2" stroke="#c0913a" stroke-width="1" fill="none"/></svg></span>hello@veloraskin.com</p>
      <p class="contact__address">Suite 4, 18 Linden Row<br>Hartwell Park, NY 10021</p>
    </div>
  </section>
</main>
</body>
</html>
```